Magazine Cover & Back, Course Overview

Please read this whole description and follow directions before proceeding. Please do not submit multiple designs that look similar. If you submit multiple designs that look similar you will be disqualified and receive a poor rating. A magazine design includes a cover and back. This is a single design and should be submitted as such. Do not submit one design for the front only, then a separate design for the back, then a third mock up. Submit all as a single design. I need a magazine cover and back. The size will be standard paper size, 8-1/2" x 11". It will be used for a course overview, a summary of a boating instruction course. I have attached examples and pictures that can be used. I have also attached required content. The final designs must NOT be AI files. Text must be editable with Adobe Acrobat DC.

Target Market(s)

Military & Government

Industry/Entity Type

Military & Government

Requirements
Must have
• See attached.
Nice to have
• See attached.
Should not have
• See attached.

```html
<!DOCTYPE html>
<html lang="en">
<head>
<meta charset="utf-8">
<title>Diver Support Vessel Training – Course Overview</title>
<link rel="stylesheet" href="https://fonts.googleapis.com/css2?family=Open+Sans:wght@300;400;600;700&display=swap">
<style>
  :root {
    --bg: #ece8e1;
    --paper: #ffffff;
    --gold: #d9ad1f;
    --gold-deep: #c99a12;
    --blue: #1d3fa3;
    --navy: #1a2a6c;
    --ink-grey: #6b6b6b;
    --white: #ffffff;
  }
  * { box-sizing: border-box; margin: 0; padding: 0; }
  html, body { width: 1200px; height: 750px; overflow: hidden; }
  body {
    background: var(--bg);
    font-family: "Open Sans", sans-serif;
    position: relative;
  }
  .page {
    position: absolute;
    top: 25px;
    width: 541px;
    height: 700px;
    overflow: hidden;
  }
  .back-cover { left: 59px; background: var(--paper); }
  .front-cover { left: 600px; background: var(--gold); }

  /* Back cover */
  .back-cover .accent { position: absolute; left: 0; top: 0; }
  .photo-strip {
    position: absolute;
    left: 87px; top: 216px;
    display: flex; gap: 4px;
  }
  .photo-strip .photo {
    width: 93px; height: 114px;
    border: 2px solid var(--white);
    box-shadow: 0 1px 3px rgba(0,0,0,.25);
  }
  .photo-a { background: linear-gradient(180deg, #9cc3e8 0%, #c9cfd6 55%, #8d969f 100%); }
  .photo-b { background: linear-gradient(160deg, #2b2b2b 0%, #6a7a72 50%, #3e3f38 100%); }
  .photo-c { background: linear-gradient(180deg, #d8d8d6 0%, #a9abac 60%, #7c7f82 100%); }
  .photo-d { background: linear-gradient(180deg, #7e8c96 0%, #5c6a5c 55%, #4a5446 100%); }

  .back-brand {
    position: absolute; left: 0; width: 558px; top: 382px;
    display: flex; justify-content: center; align-items: center; gap: 10px;
  }
  .back-title {
    position: absolute; left: 200px; width: 158px; top: 418px;
    text-align: center; color: var(--blue);
    border-bottom: 1.5px solid var(--gold);
    padding-bottom: 3px;
  }
  .back-title .light { display: block; font-weight: 300; font-size: 15px; line-height: 19px; }
  .back-title .bold { display: block; font-weight: 600; font-size: 15px; line-height: 19px; }

  /* Brand lockups */
  .brand { display: flex; align-items: center; gap: 5px; color: var(--ink-grey); font-weight: 600; white-space: nowrap; }
  .brand .dot { border-radius: 50%; background: var(--navy); border: 2px solid var(--gold); flex: none; }
  .brand-sm { font-size: 7px; line-height: 8px; }
  .brand-sm .dot { width: 30px; height: 30px; }
  .brand-lg { font-size: 9px; line-height: 11px; }
  .brand-lg .dot { width: 44px; height: 44px; }

  /* Front cover */
  .logo-tab {
    position: absolute; left: 158px; top: 0;
    width: 220px; height: 70px;
    background: var(--white);
    border-radius: 0 0 6px 6px;
    box-shadow: 0 2px 4px rgba(0,0,0,.25);
    display: flex; align-items: center; justify-content: center; gap: 10px;
    padding: 0 8px;
  }
  .cover-title {
    position: absolute; left: 0; width: 541px; top: 106px;
    text-align: center; color: var(--blue);
  }
  .cover-title .light { display: block; font-weight: 300; font-size: 40px; line-height: 48px; letter-spacing: -0.5px; }
  .cover-title .bold { display: block; font-weight: 700; font-size: 40px; line-height: 46px; letter-spacing: -0.5px; }

  .highlights {
    position: absolute; top: 232px; left: 30px;
    list-style: none;
  }
  .highlights li {
    position: absolute; top: 0;
    border-left: 1.5px solid var(--white);
    padding-left: 6px;
    color: var(--white); font-weight: 600;
    font-size: 7px; line-height: 9px;
    height: 46px;
  }
  .highlights li:nth-child(1) { left: 0;   width: 78px; top: 6px; }
  .highlights li:nth-child(2) { left: 82px; width: 70px; top: 4px; }
  .highlights li:nth-child(3) { left: 156px; width: 126px; top: 2px; }
  .highlights li:nth-child(4) { left: 286px; width: 60px; top: 0; }
  .highlights li:nth-child(5) { left: 352px; width: 60px; top: 0; }

  .hero-photo {
    position: absolute; left: 32px; top: 294px;
    width: 509px; height: 363px;
    clip-path: polygon(0 0, 100% 0, 100% 100%, 94px 100%, 0 267px);
    background: linear-gradient(180deg, #3f8fe0 0%, #76b2ec 38%, #7b7a6c 44%, #24528f 52%, #c9ccd0 68%, #1c4a86 90%, #163d72 100%);
  }
</style>
</head>
<body>

<section class="page back-cover" aria-label="Back cover">
  <svg class="accent" width="541" height="400" viewBox="0 0 541 400" aria-hidden="true">
    <polygon points="225,6 240,0 231,60 225,135" fill="var(--blue)"/>
    <polygon points="228,6 350,3 350,369" fill="var(--gold)"/>
    <polygon points="290,5 350,3 350,369" fill="var(--gold-deep)" opacity=".35"/>
  </svg>

  <div class="photo-strip">
    <div class="photo photo-a" role="img" aria-label="Sailor at the helm station on the open deck"></div>
    <div class="photo photo-b" role="img" aria-label="Crew member boarding through the cabin door"></div>
    <div class="photo photo-c" role="img" aria-label="Helm console with steering wheel and controls"></div>
    <div class="photo photo-d" role="img" aria-label="Trainees operating throttle controls on deck"></div>
  </div>

  <div class="back-brand">
    <div class="brand brand-sm"><span class="dot"></span><span>Selvaro<br>Boat Training</span></div>
    <div class="brand brand-sm"><span>Quellstone<br>Marine Services, LLC</span></div>
  </div>

  <h2 class="back-title">
    <span class="light">DIVER SUPPORT</span>
    <span class="bold">VESSEL TRAINING</span>
  </h2>
</section>

<section class="page front-cover" aria-label="Front cover">
  <div class="logo-tab">
    <div class="brand brand-lg"><span class="dot"></span><span>Selvaro<br>Boat Training</span></div>
    <div class="brand brand-lg"><span>Quellstone<br>Marine Services, LLC</span></div>
  </div>

  <h1 class="cover-title">
    <span class="light">DIVER SUPPORT</span>
    <span class="bold">VESSEL TRAINING</span>
  </h1>

  <ul class="highlights">
    <li>To assist Navy Sailors with Becoming More Proficient Coxswains</li>
    <li>Focused on Safety &amp; Close-Quarters Maneuvering</li>
    <li>Custom Made Course for Specific Users, Scenarios and Vessels Based on OIC Involvement, Client Feedback and After Action Reviews</li>
    <li>Taught by Reputable USCG Licensed Boat Captains</li>
    <li>Taught by Reputable USCG Licensed Boat Captains</li>
  </ul>

  <div class="hero-photo" role="img" aria-label="Grey diver support vessel flying a flag, underway on a blue harbor with a wooded shoreline"></div>
</section>

</body>
</html>
```